Rusty Clem's BBQ is an online seasoning and other food sales business.

I need a website and store to launch this new business. The site must be compatible to smart phones. Most of the marketing will be done through short comedic social media videos that are unrelated to cooking for entertainment purposes. I will also have cooking instructional videos. I will sell merchandise in the future. Products for sale now will be my Beef Rub and Pork Rub. In 2 months I will have an All Seasoning and Cajun Seasoning. Later this year I will add Rusty Clem's Ranch Beans and a BBQ sauce along with merchandise. I have a logo and labels designs for the seasonings. I will upload pictures of the bottles soon. I do not want this to look like a generic BBQ website because my products are not inclusive to smoking meat. No pigs or cartoon pictures on my website besides my logo. Stock photos of brisket, pork butt, ribs and chicken are welcome. The company is fun and entertaining unlike any seasoning in this world. We will make you laugh and happy through our products and videos. I had to use Rusty Clem's BBQ name due to trademark issue. Rusty Clem's is already trademarked. I'm trademarking Rusty Clem's BBQ. I'm not a huge fan of the BBQ part because it may deter some people from buying the product thinking it only for smoking meat. The roots of my company came from smoking delicious meets as a hobby and small catering jobs. I want people to use this on everything from eggs to soups, stews, vegetables, pastas, beans and many more side dishes. If you eat meat prepared in any way, these seasonings are for you. I'm more than happy to get you other pictures of meat and add content as required. I'm just setting up this company and will get you the required information upon request. I attached a sample of a blue and green label for the All Seasoning which is not finalized yet. I will use the blue label version with updated nutrient facts and ingredients.

```html
<!DOCTYPE html>
<html lang="en">
<head>
<meta charset="utf-8">
<title>Rusty Clem's BBQ</title>
<link href="https://fonts.googleapis.com/css2?family=Bebas+Neue&family=Alegreya+Sans:wght@400;500;700;800&display=swap" rel="stylesheet">
<style>
:root{
  --red:#c23b1f;
  --red-dark:#a8301a;
  --cream:#f1ebdf;
  --card:#f7f5f1;
  --ink:#1b1411;
  --muted:#5c4d44;
  --blue:#2d5aa5;
  --dark:#2a1d18;
  --white:#ffffff;
}
*{margin:0;padding:0;box-sizing:border-box}
html,body{width:1200px;height:1200px;overflow:hidden;background:#000}
body{font-family:"Alegreya Sans",sans-serif;color:var(--ink);position:relative}
.page{position:absolute;left:447px;top:4px;width:492px;height:1926px;background:var(--cream);transform:scale(.6211);transform-origin:0 0;overflow:hidden}
.abs{position:absolute}
.display{font-family:"Bebas Neue",sans-serif;font-weight:400;letter-spacing:.3px;line-height:1}
.h2{font-size:24px;color:var(--ink)}
.btn{position:absolute;display:flex;align-items:center;justify-content:center;gap:3px;font-size:6.5px;font-weight:800;text-transform:uppercase;border-radius:3px;letter-spacing:.2px}
.btn-solid{background:var(--red);color:var(--white)}
.btn-line{border:1px solid var(--red);color:var(--red);background:transparent}
.sq{display:inline-block;width:6px;height:6px;background:currentColor}
.dots{position:absolute;display:flex;gap:4px}
.dots i{width:4px;height:4px;border-radius:50%;background:#cfc7bb}
.dots i.on{background:var(--ink)}
.photo{position:absolute}

.hero{position:absolute;left:0;top:0;width:492px;height:310px}
.hero-photo{position:absolute;inset:0;background:linear-gradient(135deg,#3b2722 0%,#5a2e27 45%,#3a2420 70%,#1f1512 100%)}
.nav{position:absolute;left:34px;top:26px;width:423px;height:31px;background:var(--white);border-radius:3px;font-size:6.5px;font-weight:700}
.nav span{position:absolute;top:12px}
.logo-disc{position:absolute;left:184px;top:-16px;width:56px;height:56px;border-radius:50%;background:var(--white);display:flex;align-items:center;justify-content:center;text-align:center;font-size:9px;font-weight:800;color:var(--red);line-height:1}
.cart{position:absolute;left:388px;top:7px;width:17px;height:17px;border-radius:50%;background:var(--red)}
.hero h1{position:absolute;left:35px;top:103px;font-size:30px;color:var(--white);line-height:1.1}
.hero p{position:absolute;left:35px;top:172px;width:145px;font-size:8.5px;color:var(--white);line-height:1.6;font-weight:500}
.btn-ghost{border:1px solid var(--white);color:var(--white)}

.pcard{position:absolute;top:393px;width:137px;height:190px;background:var(--card);border-radius:4px;text-align:center}
.pcard .img{position:absolute;left:38px;top:10px;width:60px;height:110px;border-radius:4px}
.rating{position:absolute;right:8px;top:8px;font-size:6px;background:var(--white);padding:2px 4px;border-radius:6px;font-weight:700}
.rating b{color:#f2b705}
.pname{position:absolute;left:0;right:0;top:125px;font-size:8.5px;font-weight:500}
.price{position:absolute;left:0;right:0;top:137px;font-size:11px;font-weight:700;color:var(--blue)}
.soon{position:absolute;top:689px;width:101px;height:101px;background:var(--card);border-radius:4px;text-align:center}
.soon .img{position:absolute;left:35px;top:-20px;width:31px;height:60px;border-radius:3px}
.soon .pname{top:52px;font-size:8.5px}

.flavors{position:absolute;left:0;top:828px;width:492px;height:345px}
.flav{position:absolute;width:101px;height:101px;background:var(--card);border-radius:4px;text-align:center}
.flav .ic{position:absolute;left:32px;top:12px;width:37px;height:37px;border-radius:50%;background:var(--red)}
.flav .ic::after{content:"";position:absolute;left:11px;top:11px;width:15px;height:15px;border-radius:50%;border:2.5px solid var(--white)}
.flav h4{position:absolute;left:0;right:0;top:55px;font-size:8px;font-weight:700}
.flav p{position:absolute;left:14px;right:14px;top:67px;font-size:5px;font-weight:700;line-height:1.6}

.recipe{position:absolute;top:1200px;width:123px;height:101px;border-radius:5px;background:radial-gradient(circle at 50% 45%,#c49a6a 0%,#8a5a33 40%,#3b4a2a 100%);color:var(--white)}
.recipe small{position:absolute;left:8px;top:78px;font-size:4.5px}
.recipe b{position:absolute;left:8px;top:84px;font-size:8px;font-weight:700}
.recipe em{position:absolute;right:8px;top:86px;font-size:4.5px;font-style:normal}
.recipe .play{position:absolute;left:52px;top:40px;width:17px;height:17px;background:var(--white)}

.quote{position:absolute;top:1376px;width:137px;height:72px;background:var(--card);border-radius:4px}
.quote p{position:absolute;left:7px;right:6px;top:10px;font-size:5px;font-weight:500;line-height:1.9}
.avatar{position:absolute;left:7px;top:50px;width:14px;height:14px;border-radius:50%;background:#6a5a50}
.who{position:absolute;left:26px;top:51px;font-size:5px;font-weight:700;line-height:1.2}
.who span{display:block;color:var(--blue);font-weight:500;font-size:4.2px}

.video{position:absolute;top:1540px;width:208px;height:126px;border-radius:5px;color:var(--white)}
.video b{position:absolute;left:8px;top:97px;font-size:8px;font-weight:500}
.video span{position:absolute;left:8px;top:109px;font-size:6px}

.footer{position:absolute;left:0;top:1721px;width:492px;height:205px;background:var(--red);color:var(--white)}
.footer h5{font-size:6px;font-weight:700;position:absolute}
.footer ul{list-style:none;position:absolute;font-size:5.5px;line-height:14.5px}
.email{position:absolute;left:330px;top:19px;width:128px;height:18px;border:1px solid var(--white);border-radius:3px;overflow:hidden}
.email span{position:absolute;left:8px;top:5px;font-size:5px;color:var(--muted)}
.email .field{position:absolute;left:0;top:0;width:86px;height:100%;background:var(--cream)}
.email .submit{position:absolute;right:0;top:0;width:42px;height:100%;background:var(--red);font-size:5px;text-align:center;line-height:16px}
</style>
</head>
<body>
<div class="page">

  <section class="hero">
    <div class="hero-photo" role="img" aria-label="Close-up of a seasoned beef roast covered in rub with rosemary"></div>
    <div class="photo" role="img" aria-label="Two seasoning bottles, the Beef Rub and the Pork Rub" style="left:285px;top:90px;width:180px;height:190px;background:linear-gradient(160deg,#e9e3dc 0%,#b7452c 45%,#7b1e14 100%);border-radius:10px;opacity:.92"></div>
    <svg class="abs" style="left:0;top:286px" width="492" height="30" viewBox="0 0 492 30">
      <path d="M0 14 L20 8 L38 16 L60 6 L84 12 L110 4 L130 14 L158 8 L180 16 L205 6 L230 12 L256 5 L280 14 L305 7 L330 15 L356 6 L380 13 L404 5 L430 15 L455 8 L478 14 L492 10 L492 30 L0 30Z" fill="var(--cream)"/>
    </svg>
    <nav class="nav">
      <span style="left:17px">Products</span>
      <span style="left:58px">Videos</span>
      <span style="left:91px">Recipes</span>
      <span style="left:127px">About</span>
      <div class="logo-disc">Rusty<br>Clem's<br>BBQ</div>
      <span style="left:260px">FAQ's</span>
      <span style="left:289px">Contact Us</span>
      <svg class="abs" style="left:350px;top:11px" width="9" height="9" viewBox="0 0 9 9"><circle cx="3.8" cy="3.8" r="3" fill="none" stroke="var(--red)" stroke-width="1.1"/><path d="M6 6 L8.5 8.5" stroke="var(--red)" stroke-width="1.1"/></svg>
      <svg class="abs" style="left:369px;top:11px" width="9" height="9" viewBox="0 0 9 9"><circle cx="4.5" cy="2.8" r="2" fill="none" stroke="var(--ink)" stroke-width="1"/><path d="M1 8.5 Q4.5 4 8 8.5" fill="none" stroke="var(--ink)" stroke-width="1"/></svg>
      <div class="cart"></div>
    </nav>
    <h1 class="display">Dare your taste buds.<br>Season everything</h1>
    <p>Bold BBQ rubs for ribs, eggs, pasta, soups — and everything in between.</p>
    <div class="btn btn-solid" style="left:36px;top:207px;width:68px;height:20px">Buy now →</div>
    <div class="btn btn-ghost" style="left:110px;top:207px;width:68px;height:20px">Watch video ▸</div>
  </section>

  <h2 class="display h2 abs" style="left:34px;top:358px">Featured Product</h2>
  <div class="btn btn-line" style="left:388px;top:355px;width:69px;height:20px">View all</div>

  <div class="pcard" style="left:34px">
    <div class="img" role="img" aria-label="Beef rub bottle" style="background:linear-gradient(180deg,#2a2a2a 0%,#e7e1da 20%,#d9572c 60%,#efe7dc 100%)"></div>
    <div class="rating"><b>★</b> 4.8</div>
    <div class="pname">Trailhand Beef Rub</div>
    <div class="price">$12.95</div>
    <div class="btn btn-solid" style="left:7px;top:157px;width:123px;height:20px">Add to cart <i class="sq"></i></div>
  </div>
  <div class="pcard" style="left:177px">
    <div class="img" role="img" aria-label="Pork rub bottle" style="background:linear-gradient(180deg,#1c1c1c 0%,#b8301f 40%,#7a1a12 100%)"></div>
    <div class="rating"><b>★</b> 4.8</div>
    <div class="pname">Campfire Pork Rub</div>
    <div class="price">$12.99</div>
    <div class="btn btn-line" style="left:7px;top:157px;width:123px;height:20px">Add to cart <i class="sq"></i></div>
  </div>
  <div class="pcard" style="left:321px">
    <div class="img" role="img" aria-label="Cajun seasoning bottle" style="background:linear-gradient(180deg,#e8702a 0%,#c9461f 60%,#8a2a14 100%)"></div>
    <div class="rating"><b>★</b> 4.8</div>
    <div class="pname">Cajun Seasoning</div>
    <div class="price">$12.99</div>
    <div class="btn btn-line" style="left:7px;top:157px;width:123px;height:20px">Add to cart <i class="sq"></i></div>
  </div>
  <div class="dots" style="left:234px;top:598px"><i></i><i class="on"></i><i></i></div>

  <h2 class="display h2 abs" style="left:34px;top:638px">Coming Soon</h2>
  <div class="soon" style="left:34px">
    <div class="img" role="img" aria-label="All seasoning bottle" style="background:linear-gradient(180deg,#e07a2a,#7a9a3a)"></div>
    <div class="pname">All Seasoning</div>
    <div class="btn btn-line" style="left:15px;top:69px;width:71px;height:21px">Notify me ●</div>
  </div>
  <div class="soon" style="left:142px">
    <div class="img" role="img" aria-label="Cajun seasoning bottle" style="background:linear-gradient(180deg,#e07a2a,#7a9a3a)"></div>
    <div class="pname">Cajun Seasoning</div>
    <div class="btn btn-line" style="left:15px;top:69px;width:71px;height:21px">Notify me ●</div>
  </div>
  <div class="soon" style="left:249px">
    <div class="img" role="img" aria-label="Rusty Clem's Ranch Beans can" style="left:29px;width:43px;height:58px;background:linear-gradient(180deg,#3c8f3a,#1f2a3a)"></div>
    <div class="pname">Cajun Seasoning</div>
    <div class="btn btn-line" style="left:15px;top:69px;width:71px;height:21px">Notify me ●</div>
  </div>
  <div class="soon" style="left:357px">
    <div class="img" role="img" aria-label="BBQ sauce bottle" style="left:42px;width:18px;background:linear-gradient(180deg,#5a2a14,#b8451f)"></div>
    <div class="pname">BBQ Sauce</div>
    <div class="btn btn-line" style="left:15px;top:69px;width:71px;height:21px">Notify me ●</div>
  </div>

  <section class="flavors">
    <svg class="abs" style="left:0;top:0" width="492" height="345" viewBox="0 0 492 345">
      <path d="M0 10 L30 6 L50 12 L80 4 L110 12 L140 6 L170 14 L200 5 L230 12 L262 6 L290 14 L320 6 L350 12 L380 4 L410 12 L440 6 L470 13 L492 8 L492 330 Q480 322 468 330 Q456 338 444 330 Q432 322 420 330 Q408 338 396 330 Q384 322 372 330 Q360 338 348 330 Q336 322 324 330 Q312 338 300 330 Q288 322 276 330 Q264 338 252 330 Q240 322 228 330 Q216 338 204 330 Q192 322 180 330 Q168 338 156 330 Q144 322 132 330 Q120 338 108 330 Q96 322 84 330 Q72 338 60 330 Q48 322 36 330 Q24 338 12 330 Q6 326 0 330Z" fill="var(--red)"/>
    </svg>
    <div class="photo" role="img" aria-label="Raw tomahawk steak with rosemary and herbs" style="left:335px;top:0;width:115px;height:78px;border-radius:40%;background:radial-gradient(circle,#8b1e24 0%,#5e1616 55%,rgba(94,22,22,0) 72%)"></div>
    <h2 class="display abs" style="left:33px;top:52px;font-size:24px;color:var(--white)">Explore Our Flavors</h2>
  </section>
  <div class="flav" style="left:34px;top:914px"><div class="ic"></div><h4>Eggs</h4><p>Wake up your breakfast with a smoky kick that'll ruin plain omelets forever.</p></div>
  <div class="flav" style="left:142px;top:914px"><div class="ic"></div><h4>Pasta</h4><p>Wake up your breakfast with a smoky kick that'll ruin plain omelets forever.</p></div>
  <div class="flav" style="left:250px;top:914px"><div class="ic"></div><h4>Veggies</h4><p>Wake up your breakfast with a smoky kick that'll ruin plain omelets forever.</p></div>
  <div class="flav" style="left:358px;top:914px"><div class="ic"></div><h4>Meat</h4><p>Wake up your breakfast with a smoky kick that'll ruin plain omelets forever.</p></div>
  <div class="flav" style="left:34px;top:1023px"><div class="ic"></div><h4>Soups &amp; Stews</h4><p>Wake up your breakfast with a smoky kick that'll ruin plain omelets forever.</p></div>
  <div class="flav" style="left:142px;top:1023px"><div class="ic"></div><h4>Grill</h4><p>Wake up your breakfast with a smoky kick that'll ruin plain omelets forever.</p></div>
  <div class="flav" style="left:250px;top:1023px"><div class="ic"></div><h4>Tomato</h4><p>Wake up your breakfast with a smoky kick that'll ruin plain omelets forever.</p></div>
  <div class="flav" style="left:358px;top:1023px"><div class="ic"></div><h4>Chicken</h4><p>Wake up your breakfast with a smoky kick that'll ruin plain omelets forever.</p></div>

  <h2 class="display h2 abs" style="left:34px;top:1197px;line-height:1.2">Cooking<br>Instructions</h2>
  <div class="dots" style="left:34px;top:1261px"><i></i><i class="on"></i><i></i></div>
  <div class="btn btn-line" style="left:34px;top:1280px;width:69px;height:22px">View all</div>
  <div class="recipe" role="img" aria-label="Bowl of beef rub brisket stew" style="left:171px"><div class="play"></div><small>Intermediate</small><b>Beef rub brisket</b><em>● 12 min</em></div>
  <div class="recipe" role="img" aria-label="Bowl of beef rub brisket stew" style="left:300px"><div class="play"></div><small>Intermediate</small><b>Beef rub brisket</b><em>● 12 min</em></div>
  <div class="recipe" role="img" aria-label="Bowl of beef rub brisket stew" style="left:430px"><div class="play"></div><small>Intermediate</small><b>Beef rub brisket</b></div>

  <h2 class="display h2 abs" style="left:34px;top:1335px">What the Crew Says</h2>
  <div class="btn btn-line" style="left:388px;top:1333px;width:69px;height:21px">View all</div>
  <div class="quote" style="left:-110px"></div>
  <div class="quote" style="left:34px"><p>Eget egestas purus viverra accumsan. Eget est lorem ipsum dolor sit amet consectetur adipiscing. At lectus urna duis convallis convallis tellus id interdum velit.</p><div class="avatar"></div><div class="who">Marla Quinn<span>Home Chef &amp; Rebel</span></div></div>
  <div class="quote" style="left:177px"><p>Eget egestas purus viverra accumsan. Eget est lorem ipsum dolor sit amet consectetur adipiscing. At lectus urna duis convallis convallis tellus id interdum velit.</p><div class="avatar"></div><div class="who">Marla Quinn<span>Home Chef &amp; Rebel</span></div></div>
  <div class="quote" style="left:321px"><p>Eget egestas purus viverra accumsan. Eget est lorem ipsum dolor sit amet consectetur adipiscing. At lectus urna duis convallis convallis tellus id interdum velit.</p><div class="avatar"></div><div class="who">Marla Quinn<span>Home Chef &amp; Rebel</span></div></div>
  <div class="quote" style="left:465px"></div>
  <div class="dots" style="left:234px;top:1463px"><i></i><i class="on"></i><i></i></div>

  <h2 class="display h2 abs" style="left:33px;top:1505px">Entertainment Videos</h2>
  <div class="btn btn-line" style="left:388px;top:1504px;width:69px;height:21px">View all</div>
  <div class="video" role="img" aria-label="Two men in aprons and hats in a barbecue workshop" style="left:34px;background:linear-gradient(135deg,#5d6670 0%,#2e3640 55%,#161b21 100%)"><b>Why your eggs are boring</b><span>◎ 30K views • 2 days ago</span></div>
  <div class="video" role="img" aria-label="Smoky grilled meat close-up" style="left:249px;background:linear-gradient(135deg,#4a4440 0%,#5a3224 45%,#2a1a14 100%)"><b>Why I quit my job to season things</b><span>▶ 10K views • 2 days ago</span></div>
  <div class="dots" style="left:234px;top:1682px"><i></i><i class="on"></i><i></i></div>

  <footer class="footer">
    <div class="abs" style="left:34px;top:18px;font-size:8.5px;font-weight:500">Subscribe to our newsletter</div>
    <div class="abs" style="left:34px;top:30px;font-size:5px">Join our community and receive exclusive offers, deals and recipes to spice up your meals!</div>
    <div class="email"><div class="field"></div><span>Email address</span><div class="submit">Submit</div></div>
    <div class="abs" style="left:34px;top:48px;width:424px;height:1px;background:rgba(255,255,255,.35)"></div>
    <div class="abs" style="left:34px;top:63px;font-size:8px;font-weight:800;line-height:1.05">Rusty<br>Clem's BBQ</div>
    <p class="abs" style="left:34px;top:98px;width:125px;font-size:5px;line-height:1.9">Eget egestas purus viverra accumsan. Eget est lorem ipsum dolor sit amet consectetur adipiscing. At lectus urna duis convallis convallis tellus id interdum velit.</p>
    <div class="abs" style="left:34px;top:132px;display:flex;gap:5px">
      <i style="width:5px;height:5px;border-radius:50%;background:#fff"></i><i style="width:5px;height:5px;border-radius:50%;background:#fff"></i><i style="width:5px;height:5px;border-radius:50%;background:#fff"></i><i style="width:5px;height:5px;border-radius:50%;background:#fff"></i><i style="width:5px;height:5px;border-radius:50%;background:#fff"></i>
    </div>
    <h5 style="left:183px;top:83px">Shop</h5>
    <ul style="left:183px;top:96px"><li>Beef Rub</li><li>Pork Rub</li><li>All Seasoning (Soon)</li><li>Cunjun (Soon)</li><li>Merchandise (Soon)</li></ul>
    <h5 style="left:258px;top:83px">Company</h5>
    <ul style="left:258px;top:96px"><li>About Us</li><li>FAQ's</li><li>Recipes</li><li>Testimonials</li><li>Careers</li></ul>
    <h5 style="left:312px;top:83px">Legal</h5>
    <ul style="left:312px;top:96px"><li>Privacy Policy</li><li>Return Policy</li><li>Terms &amp; Conditions</li><li>Cookies Policy</li></ul>
    <h5 style="left:383px;top:81px">Need Assistance</h5>
    <ul style="left:383px;top:96px;line-height:10.5px"><li>hello@rustyclemsbbq.com</li><li>118 Cedar Hollow Rd Austin,</li><li>TX 78701</li><li>(+01) 555 014 2290</li></ul>
    <div class="abs" style="left:0;right:0;top:189px;text-align:center;font-size:4.5px">Copyright © 2025 Rusty Clem's BBQ - All Rights Reserved.</div>
  </footer>
</div>
</body>
</html>
```